Fun, Colorful, Classy ,& Stylish Wine Bacholorette Labels

Thanks For Stopping By, My Hope is That we Can Knock this out of The Park :)
Ok, So Here is Our Big Idea.

We are going to be launching another product on zelvio that are similar to these below.
https://www.zelvio.com/Toast-Tags-Proposal-Soiree-Hen-Night/item/Q73KXW82PD/ref=lst_2_4?s=home-decor&ie=UTF8&qid=8846213057&sr=2-4&keywords=bridal+wine+labels&itemID=73pqRtuWmZa&preST=SY300_QL70&itemSrc=srch
https://www.zelvio.com/Wow-Look-Whos-Tying-Knot-Proposal/item/Q92MZL47VN/ref=rel_sim_41_3?_encoding=UTF8&rel_i=Q92MZL47VN&rel_r=KPWQX83JZL27NM46D19F&rel_w=tgQ4r&rel_wg=v9LpD&psc=1&refRID=KPWQX83JZL27NM46D19F
https://www.zelvio.com/Hen-Night-Nuptial-Vino-Flask-Tags/item/Q58TRW63KB/ref=rel_sim_41_2?_encoding=UTF8&rel_i=Q58TRW63KB&rel_r=KPWQX83JZL27NM46D19F&rel_w=tgQ4r&rel_wg=v9LpD&psc=1&refRID=KPWQX83JZL27NM46D19F

We are going to do a few Styles.
1 Bachelorette , Engagement Party - Bridal Gift - Funny - 6Pc

We are planning to do a few more but let’s start with this one first.

size: 4'' x 5'' - mock up should also be done on the bottle. pick from one of the quotes below and design a label that will knock our socks off. :)

the wine bottle pics are just an example of another company that have done something similar.

T

Industry/Entity Type

Wedding

Font styles to use
Script

Colors
e667a6
ffffff
33a6d7
b768aa
e34197
fbee3d
abd036
33b8a4
6b449b

Requirements
Must have
• Colorful Humor and tasteful
Nice to have
• a creative spin on concept
Should not have
• should not be plain jane/ boring.

```html
<!DOCTYPE html>
<html lang="en">
<head>
<meta charset="utf-8">
<title>Drunk in Love – Wine Label</title>
<link rel="stylesheet" href="https://fonts.googleapis.com/css2?family=Dancing+Script:wght@600;700&display=swap">
<style>
  :root {
    --backdrop: #b3b3b3;
    --label-white: #ffffff;
    --gold-light: #e6bf78;
    --gold: #c9974a;
    --gold-deep: #a8772f;
    --rose: #e2566f;
    --rose-light: #f07a8c;
    --rose-deep: #c93c57;
  }
  * { box-sizing: border-box; margin: 0; padding: 0; }
  html, body {
    width: 1200px;
    height: 923px;
    overflow: hidden;
    background: var(--backdrop);
  }
  .label {
    position: absolute;
    left: 256px;
    top: 31px;
    width: 688px;
    height: 860px;
    background: var(--label-white);
    overflow: hidden;
  }
  .label__frame {
    position: absolute;
    inset: 0;
    width: 100%;
    height: 100%;
  }
  .label__title {
    position: absolute;
    font-family: "Dancing Script", cursive;
    line-height: 1;
    white-space: nowrap;
    -webkit-background-clip: text;
    background-clip: text;
    color: transparent;
  }
  .label__title--drunk {
    left: 128px;
    top: 188px;
    font-size: 170px;
    font-weight: 700;
    transform: rotate(-5deg);
    background-image: linear-gradient(100deg, var(--gold-deep), var(--gold-light) 45%, var(--gold) 70%, var(--gold-deep));
  }
  .label__title--in {
    left: 300px;
    top: 338px;
    font-size: 120px;
    font-weight: 700;
    background-image: linear-gradient(100deg, var(--gold-deep), var(--gold-light), var(--gold));
  }
  .label__title--love {
    left: 100px;
    top: 410px;
    font-size: 230px;
    font-weight: 700;
    transform: rotate(-5deg);
    background-image:
      radial-gradient(circle at 30% 40%, var(--rose-light) 0 1px, transparent 2px),
      linear-gradient(100deg, var(--rose-deep), var(--rose) 40%, var(--rose-light) 60%, var(--rose));
    background-size: 5px 5px, 100% 100%;
  }
</style>
</head>
<body>
  <main class="label" aria-label="Drunk in Love wine label">
    <svg class="label__frame" viewBox="0 0 400 500" preserveAspectRatio="none" xmlns="http://www.w3.org/2000/svg">
      <defs>
        <linearGradient id="ornament-tone" x1="0" y1="0" x2="1" y2="1">
          <stop offset="0" stop-color="#f3e2bf"/>
          <stop offset="1" stop-color="#fbf3e3"/>
        </linearGradient>
        <linearGradient id="frame-gold" x1="0" y1="0" x2="1" y2="1">
          <stop offset="0" stop-color="#d6a85c"/>
          <stop offset="0.5" stop-color="#e9c584"/>
          <stop offset="1" stop-color="#b9863a"/>
        </linearGradient>
      </defs>

      <g class="label__ornaments">
        <polygon role="img" aria-label="Gold line-drawn leaf ornament, top left" points="0,0 140,0 140,55 91,58 0,260" fill="url(#ornament-tone)"/>
        <polygon role="img" aria-label="Gold line-drawn leaf ornament, top right" points="254,0 400,0 400,260 396,260 306,58 254,55" fill="url(#ornament-tone)"/>
        <polygon role="img" aria-label="Gold line-drawn leaf ornament, bottom left" points="0,260 91,430 144,430 150,500 0,500" fill="url(#ornament-tone)"/>
        <polygon role="img" aria-label="Gold line-drawn leaf ornament, bottom right" points="396,260 400,260 400,500 250,500 252,430 306,430" fill="url(#ornament-tone)"/>
      </g>

      <g class="label__geometry" fill="none" stroke="url(#frame-gold)" stroke-width="1.6" stroke-linejoin="miter">
        <polygon class="label__hexagon" points="91,58 306,58 396,260 306,430 91,430 0,260" fill="#ffffff"/>
        <polyline class="label__peak label__peak--top" points="140,56 197,0 254,56"/>
        <polyline class="label__peak label__peak--bottom" points="144,430 197,487 252,430"/>
      </g>

      <g class="label__gem" fill="none" stroke="#c9974a" stroke-width="1" stroke-linejoin="round">
        <polygon points="272,349 311,349 326,364 291,411 257,364"/>
        <polyline points="257,364 326,364"/>
        <polyline points="272,349 280,364 291,411 303,364 311,349"/>
        <polyline points="280,364 291,349 303,364"/>
      </g>
    </svg>

    <h1 class="label__heading">
      <span class="label__title label__title--drunk">Drunk</span>
      <span class="label__title label__title--in">in</span>
      <span class="label__title label__title--love">Love</span>
    </h1>
  </main>
</body>
</html>
```